Velmora Biz Card 2019

New business card for Velmora Property Inspections. We are a residential home inspection company in Arizona.

Target Market(s)

Real Estate

Font styles to use
Sans Serif

Requirements
Must have
• Glen Mirewick
• Home Inspector
• Velmora Property Inspections, LLC
• 480-555-0172
• glen@velmora-llc.example

```html
<!DOCTYPE html>
<html lang="en">
<head>
<meta charset="utf-8">
<title>Velmora Property Inspections – Business Card</title>
<link rel="stylesheet" href="https://fonts.googleapis.com/css2?family=Lato:wght@400;700&family=Montserrat:wght@500;700&display=swap">
<style>
  :root {
    --page-bg: #ececec;
    --card-light-a: #ffffff;
    --card-light-b: #e3e4e5;
    --slate: #636567;
    --slate-dark: #55575a;
    --green: #3aae48;
    --green-dark: #2f9a3d;
    --ink: #5c5e60;
    --white: #ffffff;
    --mist: #e6e7e8;
  }
  html, body {
    margin: 0;
    width: 1200px;
    height: 1200px;
    overflow: hidden;
    background: var(--page-bg);
  }
  .card {
    position: absolute;
    left: 220px;
    width: 760px;
    height: 456px;
    box-shadow: 0 3px 6px rgba(0,0,0,0.25);
  }
  .card svg { display: block; width: 100%; height: 100%; }
  .card--front { top: 144px; }
  .card--back { top: 648px; }
  .wordmark { font-family: "Montserrat", sans-serif; font-weight: 700; letter-spacing: 0.5px; }
  .tagline { font-family: "Montserrat", sans-serif; font-weight: 500; }
  .person-name { font-family: "Lato", sans-serif; font-weight: 700; }
  .detail { font-family: "Lato", sans-serif; font-weight: 400; }
</style>
</head>
<body>

<section class="card card--front" aria-label="Business card front">
  <svg viewBox="0 0 634 380" xmlns="http://www.w3.org/2000/svg">
    <defs>
      <linearGradient id="front-paper" x1="0" y1="0" x2="1" y2="1">
        <stop offset="0" stop-color="var(--card-light-b)"/>
        <stop offset="0.45" stop-color="var(--card-light-a)"/>
        <stop offset="1" stop-color="var(--card-light-b)"/>
      </linearGradient>
      <linearGradient id="front-slate" x1="0" y1="0" x2="1" y2="0">
        <stop offset="0" stop-color="var(--slate-dark)"/>
        <stop offset="0.6" stop-color="var(--slate)"/>
        <stop offset="1" stop-color="var(--slate-dark)"/>
      </linearGradient>
    </defs>
    <rect class="paper" width="634" height="380" fill="url(#front-paper)"/>
    <polygon class="accent-green" points="0,245 367,177 0,281" fill="var(--green)"/>
    <polygon class="slate-band" points="0,288 634,105 634,380 0,380" fill="url(#front-slate)"/>

    <rect class="brand-square" x="52" y="62" width="40" height="40" fill="var(--green)"/>
    <text class="wordmark" x="104" y="92" font-size="30" fill="var(--ink)">VELMORA</text>
    <text class="tagline" x="105" y="110" font-size="12.5" fill="var(--ink)">PROPERTY INSPECTIONS, LLC</text>

    <text class="person-name" x="582" y="228" font-size="24" fill="var(--white)" text-anchor="end">Glen Mirewick</text>
    <text class="detail" x="582" y="250" font-size="18.5" fill="var(--mist)" text-anchor="end">Home Inspector</text>

    <text class="detail" x="51" y="312" font-size="15" fill="var(--white)">4410 S. Orchard Ln.</text>
    <text class="detail" x="51" y="335" font-size="15" fill="var(--white)">Tempe, AZ 85280</text>

    <text class="detail" x="564" y="290" font-size="14.5" fill="var(--white)" text-anchor="end">480-555-0172</text>
    <text class="detail" x="564" y="312" font-size="14.5" fill="var(--white)" text-anchor="end">glen@velmora-llc.example</text>
    <text class="detail" x="564" y="333" font-size="14.5" fill="var(--white)" text-anchor="end">www.velmora-llc.example</text>

    <g class="icon icon--phone" fill="var(--mist)" transform="translate(571,280)">
      <path d="M2 1 L4.5 1 L5.5 3.5 L4 4.8 C4.8 6.5 6 7.8 7.5 8.5 L8.8 7 L11 8 L11 10.5 C11 11 10.5 11.5 10 11.5 C5 11 1.5 7.5 1 2.5 C1 1.6 1.5 1 2 1 Z"/>
    </g>
    <g class="icon icon--mail" transform="translate(571,303)">
      <rect x="0" y="0" width="11" height="8" fill="var(--mist)"/>
      <path d="M0 0 L5.5 4.5 L11 0" fill="none" stroke="var(--slate)" stroke-width="1"/>
    </g>
    <g class="icon icon--web" transform="translate(576.5,328.5)">
      <circle r="5.5" fill="var(--mist)"/>
      <path d="M-5.5 0 H5.5 M0 -5.5 V5.5" stroke="var(--slate)" stroke-width="0.9"/>
    </g>
  </svg>
</section>

<section class="card card--back" aria-label="Business card back">
  <svg viewBox="0 0 634 380" xmlns="http://www.w3.org/2000/svg">
    <defs>
      <radialGradient id="back-slate" cx="0.5" cy="0.45" r="0.7">
        <stop offset="0" stop-color="#6c6e70"/>
        <stop offset="1" stop-color="var(--slate-dark)"/>
      </radialGradient>
      <linearGradient id="silver-streak" x1="0" y1="1" x2="1" y2="0">
        <stop offset="0" stop-color="#3c3e40"/>
        <stop offset="0.45" stop-color="#9a9c9e"/>
        <stop offset="0.8" stop-color="#f4f4f4"/>
        <stop offset="1" stop-color="#ffffff"/>
      </linearGradient>
    </defs>
    <rect class="paper" width="634" height="380" fill="url(#back-slate)"/>
    <polygon class="silver-streak" points="0,378 585,272 240,380 0,380" fill="url(#silver-streak)"/>
    <polygon class="accent-green" points="634,262 634,380 235,380 590,276" fill="var(--green)"/>

    <rect class="brand-square" x="292" y="88" width="50" height="50" fill="var(--green)"/>
    <text class="wordmark" x="317" y="217" font-size="34" fill="var(--white)" text-anchor="middle">VELMORA</text>
    <text class="tagline" x="317" y="237" font-size="14" fill="var(--mist)" text-anchor="middle">PROPERTY INSPECTIONS, LLC</text>

    <text class="detail" x="587" y="345" font-size="15" fill="var(--white)" text-anchor="end">www.velmora-llc.example</text>
  </svg>
</section>

</body>
</html>
```